Skin care manufacturer looking for packaging design for new skin care brand.

We need a design and logo for a skin care brand to be sold at retail stores and online in the United States and Europe. The design will be for 1.7oz - 2oz serums that will not have a retail box. The name of the brand is Velvet Meadow and should be a luxurious brand that is approachable. The brand will consist of 4 face serums - Vitamin C, Collagen, Retinol and Hyaluronic Acid. Images shown are for inspiration only. Color of bottles can be varied based on design and bottles can be screen printed or labeled.
Updates

Need extra days to review

Target Market(s)

Target market is 30+ female

Industry/Entity Type

Beauty

Requirements
Must have
• Ingredient call outs + benefit. Ex: Vitamin C Brightening Serum. Packaging should be translucent

```html
<!DOCTYPE html>
<html lang="en">
<head>
<meta charset="utf-8">
<title>Velvet Meadow Serum Range</title>
<link rel="stylesheet" href="https://fonts.googleapis.com/css2?family=Josefin+Sans:wght@400;600&display=swap">
<style>
  :root {
    --page: #ffffff;
    --ink: #ffffff;
    --cap-light: #fbfbfb;
    --cap-shade: #e4e4e4;
    --collagen-top: #3fb0ac;
    --collagen-bottom: #93c28c;
    --collagen-accent: #4da89a;
    --vitc-top: #f0a572;
    --vitc-bottom: #fbd457;
    --vitc-accent: #f4b24a;
    --retinol-top: #d8747f;
    --retinol-bottom: #e6965e;
    --retinol-accent: #d9785f;
    --hyaluronic-top: #4aa3c6;
    --hyaluronic-bottom: #71bedd;
    --hyaluronic-accent: #4aa7cc;
  }
  * { margin: 0; padding: 0; box-sizing: border-box; }
  html, body { width: 1200px; height: 750px; overflow: hidden; background: var(--page); }
  body { position: relative; font-family: "Josefin Sans", "Century Gothic", sans-serif; color: var(--ink); }

  .serum { position: absolute; top: 109px; width: 152px; height: 504px; }
  .serum--collagen { left: 208px; --top: var(--collagen-top); --bottom: var(--collagen-bottom); --accent: var(--collagen-accent); }
  .serum--vitamin-c { left: 412px; --top: var(--vitc-top); --bottom: var(--vitc-bottom); --accent: var(--vitc-accent); }
  .serum--retinol { left: 616px; --top: var(--retinol-top); --bottom: var(--retinol-bottom); --accent: var(--retinol-accent); }
  .serum--hyaluronic { left: 820px; --top: var(--hyaluronic-top); --bottom: var(--hyaluronic-bottom); --accent: var(--hyaluronic-accent); }

  .dropper-bulb {
    position: absolute; left: 54px; top: 0; width: 47px; height: 95px;
    border-radius: 23px 23px 0 0;
    background: linear-gradient(90deg, var(--cap-shade), var(--cap-light) 35%, var(--cap-light) 65%, var(--cap-shade));
  }
  .dropper-collar {
    position: absolute; left: 36px; top: 93px; width: 79px; height: 67px;
    background: linear-gradient(90deg, var(--cap-shade), var(--cap-light) 30%, var(--cap-light) 70%, var(--cap-shade));
  }
  .label {
    position: absolute; left: 0; top: 160px; width: 152px; height: 344px;
    border-radius: 3px 3px 6px 6px;
    background:
      linear-gradient(90deg, rgba(0,0,0,.18), rgba(0,0,0,0) 14%, rgba(0,0,0,0) 86%, rgba(0,0,0,.18)),
      linear-gradient(180deg, var(--top), var(--bottom));
    text-align: center;
  }
  .brand-name {
    position: absolute; left: 0; right: 0; top: 112px;
    font-size: 17px; font-weight: 400; letter-spacing: 1px;
  }
  .product-name {
    position: absolute; left: 0; right: 0; top: 198px;
    font-size: 13.5px; line-height: 15px; font-weight: 400; letter-spacing: -.2px;
  }
  .product-type {
    position: absolute; left: 22px; top: 229px; width: 104px; height: 12px;
    background: var(--ink); color: var(--accent);
    font-size: 10px; line-height: 13px; font-weight: 600; letter-spacing: 1px;
  }
  .strength { position: absolute; left: 0; right: 0; top: 262px; font-size: 10px; }
  .benefits {
    position: absolute; left: 6px; right: 6px; top: 277px;
    font-size: 6px; line-height: 6.5px; letter-spacing: .1px;
  }
  .volume { position: absolute; left: 22px; top: 325px; font-size: 7px; }
</style>
</head>
<body>
  <div class="serum serum--collagen">
    <div class="dropper-bulb"></div><div class="dropper-collar"></div>
    <div class="label">
      <p class="brand-name">Velvet Meadow</p>
      <h2 class="product-name">PHYTO PLUMP<br>COLLAGEN</h2>
      <p class="product-type">SERUM</p>
      <p class="benefits">A LIGHT, REFRESHING COLLAGEN<br>SERUM WITH A VEGAN FORMLA</p>
      <p class="volume">29ML</p>
    </div>
  </div>

  <div class="serum serum--vitamin-c">
    <div class="dropper-bulb"></div><div class="dropper-collar"></div>
    <div class="label">
      <p class="brand-name">Velvet Meadow</p>
      <h2 class="product-name">BRIGHTENING<br>VITAMIN C</h2>
      <p class="product-type">SERUM</p>
      <p class="strength">3.5%</p>
      <p class="benefits">VITAMIN C + NIACINAMIDE<br>+ SALICYLIC ACID</p>
      <p class="volume">29ML</p>
    </div>
  </div>

  <div class="serum serum--retinol">
    <div class="dropper-bulb"></div><div class="dropper-collar"></div>
    <div class="label">
      <p class="brand-name">Velvet Meadow</p>
      <h2 class="product-name">SKIN RENEWAL<br>RETINOL</h2>
      <p class="product-type">SERUM</p>
      <p class="benefits">REFINES SKIN TEXTURES, INTENSIVE<br>ACNE CARE, REVIVES RADIANCE</p>
      <p class="volume">29ML</p>
    </div>
  </div>

  <div class="serum serum--hyaluronic">
    <div class="dropper-bulb"></div><div class="dropper-collar"></div>
    <div class="label">
      <p class="brand-name">Velvet Meadow</p>
      <h2 class="product-name">ULTRA PURE<br>HYALURONIC ACID</h2>
      <p class="product-type">SERUM</p>
      <p class="benefits">ULTRA HYDRATING, REPLUMPING,<br>ANTI AGING, REPAIRING</p>
      <p class="volume">29ML</p>
    </div>
  </div>
</body>
</html>
```